Family Owned and Operated Spray Foam Insulation Company needs a business card design

We're a new company based in the heart of Texas (Fort Worth). We spray foam insulation into residential houses, commercial buildings, metal buildings, etc. Spray foam insulation provides a huge reduction in energy/costs so that is what drives our market. We like the primary colors but are open to suggestions and are coming to the experts for some creativity. I'm attaching a picture of shirt mock up we have with KTL on the front to show what we were leaning towards as well as some business cards that I find striking and memorable. I'm looking for a card that is clean and professional with a bit of edge. Note: My computer won't pull up the color samples below for me to choose so it's in your hands.

Target Market(s)

Professional custom home builders, construction industry, home owners

Industry/Entity Type

Residential

Contact Information for Business Card

Name: Mark Kettle (no title) Phone #: 817-555-0148, address: 4187 larkmoor ave fort worth tx 76109, email: mark@ktlinsulation-example.com, website: ktlinsulation-example.com

Requirements
Must have
• We want the words KTL and Kettle Spray Foam Insulation showcased on the card but hopefully on opposite sides
Should not have
• Any type of spray foam gun or splatter clip art

```html
<!DOCTYPE html>
<html lang="en">
<head>
<meta charset="utf-8">
<title>Kettle Spray Foam Insulation – Business Card</title>
<link rel="stylesheet" href="https://fonts.googleapis.com/css2?family=Sorts+Mill+Goudy&family=EB+Garamond:wght@400;700&display=swap">
<style>
  :root {
    --bg: #e6e6e6;
    --card: #f6f6f6;
    --band: #e9e9e9;
    --navy: #1f2a66;
    --red: #e02a22;
    --shadow: rgba(0, 0, 0, 0.12);
  }
  * { box-sizing: border-box; margin: 0; padding: 0; }
  html, body {
    width: 1200px;
    height: 973px;
    overflow: hidden;
    background: var(--bg);
  }
  .sheet {
    width: 1200px;
    height: 973px;
    display: flex;
    flex-direction: column;
    align-items: center;
    justify-content: center;
    gap: 52px;
  }
  .card {
    position: relative;
    width: 770px;
    height: 440px;
    background:
      repeating-linear-gradient(90deg,
        var(--card) 0 38px,
        var(--band) 38px 76px);
    box-shadow: 0 6px 18px var(--shadow);
    overflow: hidden;
  }
  .wordmark {
    font-family: "EB Garamond", "Sorts Mill Goudy", serif;
    font-weight: 700;
    color: var(--navy);
    letter-spacing: 0.02em;
    line-height: 1;
  }
  .card--front .wordmark {
    position: absolute;
    inset: 0;
    display: flex;
    align-items: center;
    justify-content: center;
    font-size: 210px;
  }
  .card--back .wordmark {
    position: absolute;
    left: 60px;
    bottom: 52px;
    font-size: 92px;
  }
  .contact {
    position: absolute;
    left: 392px;
    top: 70px;
    font-family: "Sorts Mill Goudy", "EB Garamond", serif;
    color: var(--navy);
  }
  .contact__name {
    font-variant: small-caps;
    color: var(--red);
    font-size: 30px;
    line-height: 1.05;
    letter-spacing: 0.02em;
  }
  .contact__phone {
    font-size: 26px;
    line-height: 1.2;
  }
  .contact__company {
    margin-top: 22px;
    font-family: "EB Garamond", serif;
    font-weight: 700;
    font-size: 22px;
  }
  .contact__list {
    list-style: none;
    margin-top: 6px;
  }
  .contact__item {
    display: flex;
    align-items: flex-start;
    gap: 12px;
    font-size: 19px;
    line-height: 1.3;
    margin-top: 10px;
  }
  .contact__icon {
    flex: none;
    width: 22px;
    height: 22px;
    margin-top: 2px;
  }
</style>
</head>
<body>
<main class="sheet">
  <section class="card card--front" aria-label="Card front">
    <div class="wordmark">KTL</div>
  </section>

  <section class="card card--back" aria-label="Card back">
    <div class="contact">
      <p class="contact__name">Mark Kettle</p>
      <p class="contact__phone">817-555-0148</p>
      <p class="contact__company">Kettle Spray Foam Insulation</p>
      <ul class="contact__list">
        <li class="contact__item">
          <svg class="contact__icon" viewBox="0 0 22 22" aria-hidden="true">
            <circle cx="11" cy="11" r="10" fill="var(--red)"/>
            <path d="M11 5a4 4 0 0 0-4 4c0 3 4 7 4 7s4-4 4-7a4 4 0 0 0-4-4z" fill="#fff"/>
            <circle cx="11" cy="9" r="1.5" fill="var(--red)"/>
          </svg>
          <span>4187 Larkmoor Ave.<br>Fort Worth, TX 76109</span>
        </li>
        <li class="contact__item">
          <svg class="contact__icon" viewBox="0 0 22 22" aria-hidden="true">
            <circle cx="11" cy="11" r="10" fill="var(--red)"/>
            <rect x="5.5" y="7" width="11" height="8" fill="#fff"/>
            <path d="M5.5 7l5.5 4.5L16.5 7" fill="none" stroke="var(--red)" stroke-width="1.2"/>
          </svg>
          <span>mark@ktlinsulation-example.com</span>
        </li>
        <li class="contact__item">
          <svg class="contact__icon" viewBox="0 0 22 22" aria-hidden="true">
            <circle cx="11" cy="11" r="10" fill="var(--red)"/>
            <g fill="none" stroke="#fff" stroke-width="1.2">
              <circle cx="11" cy="11" r="5.5"/>
              <ellipse cx="11" cy="11" rx="2.4" ry="5.5"/>
              <path d="M5.5 11h11"/>
            </g>
          </svg>
          <span>www.ktlinsulation-example.com</span>
        </li>
      </ul>
    </div>
    <div class="wordmark">KTL</div>
  </section>
</main>
</body>
</html>
```